Elegant Gather Glow Rentals DL flyer

We run a Gather Glow Rentals business - this will be used as a business card as well.

our website is gatherglowrentals.com.au

Front page it sour logo which is attached website details - on the front it needs to say wedding and event hire needs etc..

on the back we will have a spot for 4 products but we want to say there is more so check our the website

A background in the flyer only for example like this would be good http://backdropvista.com/black-background-wallpaper_2881.html

Wedding

• nice background elegant in style pink and black is the colours

```html
<!DOCTYPE html>
<html lang="en">
<head>
<meta charset="utf-8">
<title>Gather Glow Rentals – Flyer</title>
<link rel="stylesheet" href="https://fonts.googleapis.com/css2?family=Raleway:wght@300;400;700&display=swap">
<style>
  :root {
    --paper: #ffffff;
    --paper-shade: #e4e4e4;
    --blush: #f3b4d3;
    --magenta: #e3147f;
    --magenta-light: #ec3f97;
    --magenta-deep: #c90d6e;
    --plum: #4a0a2a;
    --ink: #0b0b0b;
    --white: #ffffff;
  }
  html, body {
    margin: 0;
    padding: 0;
    width: 1200px;
    height: 2400px;
    overflow: hidden;
    background: var(--paper);
  }
  .flyer {
    position: relative;
    width: 1200px;
    height: 2400px;
    overflow: hidden;
    font-family: "Raleway", "Century Gothic", sans-serif;
    background: radial-gradient(ellipse at 50% 20%, var(--paper) 35%, var(--paper-shade) 100%);
  }
  .flyer__waves {
    position: absolute;
    inset: 0;
    width: 1200px;
    height: 2400px;
  }
  .brand {
    position: absolute;
    top: 190px;
    left: 0;
    width: 1200px;
    text-align: center;
  }
  .brand__dot {
    display: block;
    width: 200px;
    height: 200px;
    margin: 0 auto;
    border-radius: 50%;
    background: var(--magenta);
  }
  .brand__name {
    margin: 40px 0 0;
    font-size: 78px;
    font-weight: 400;
    color: var(--magenta);
    letter-spacing: 1px;
  }
  .tagline {
    position: absolute;
    top: 1170px;
    left: 60px;
    width: 1080px;
    margin: 0;
    text-align: center;
    font-size: 58px;
    font-weight: 400;
    line-height: 1.32;
    color: var(--white);
  }
  .tagline strong { font-weight: 700; }
  .contact {
    position: absolute;
    top: 1960px;
    left: 0;
    width: 1200px;
    text-align: center;
  }
  .contact__web {
    margin: 0;
    font-size: 64px;
    font-weight: 700;
    color: var(--magenta);
  }
  .contact__email {
    margin: 10px 0 0;
    font-size: 47px;
    font-weight: 400;
    color: var(--magenta);
  }
  .contact__phone {
    display: inline-block;
    margin-top: 80px;
    width: 620px;
    height: 122px;
    line-height: 122px;
    border-radius: 12px;
    background: linear-gradient(to bottom, var(--magenta-light), var(--magenta-deep));
    font-size: 84px;
    font-weight: 700;
    color: var(--white);
    letter-spacing: 1px;
  }
</style>
</head>
<body>
  <main class="flyer">
    <svg class="flyer__waves" viewBox="0 0 1200 2400" aria-hidden="true">
      <path d="M0 760 C 300 690, 700 880, 1200 700 L1200 2400 L0 2400 Z" fill="var(--blush)"/>
      <path d="M0 860 C 350 760, 760 920, 1200 790 L1200 2400 L0 2400 Z" fill="var(--magenta)"/>
      <path d="M0 1020 C 420 880, 820 1020, 1200 900 L1200 1460 C 820 1380, 420 1470, 0 1520 Z" fill="var(--magenta-light)" opacity="0.55"/>
      <path d="M0 1660 C 380 1560, 820 1720, 1200 1610 L1200 2400 L0 2400 Z" fill="var(--magenta-deep)"/>
      <path d="M0 1790 C 420 1740, 800 1880, 1200 1770 L1200 2400 L0 2400 Z" fill="var(--plum)"/>
      <path d="M0 1870 C 420 1830, 820 1940, 1200 1850 L1200 2400 L0 2400 Z" fill="var(--ink)"/>
    </svg>

    <header class="brand">
      <span class="brand__dot"></span>
      <h1 class="brand__name">Gather Glow Rentals</h1>
    </header>

    <p class="tagline">A range of wedding packages and equipment to make your day special <strong>without the extra cost.</strong></p>

    <footer class="contact">
      <p class="contact__web">gatherglowrentals.com.au</p>
      <p class="contact__email">info@gatherglowrentals.com.au</p>
      <div class="contact__phone">0400555218</div>
    </footer>
  </main>
</body>
</html>
```